Love pets? Create a veterinary business card that aligns with our new revamped website.

Greetings! We are a five-doctor veterinary hospital that seeks your expertise in designing a new business card that harmonizes with our recently revitalized website: www.lmcr.net. The card should feature our logo, the five doctors, operating hours, contact information, and communicate our purpose and personality.

Contact Information for Business Card

TBA

```html
<!DOCTYPE html>
<html lang="en">
<head>
<meta charset="utf-8">
<title>Lone Maple Creek Veterinary Hospital – Business Card</title>
<link href="https://fonts.googleapis.com/css2?family=Roboto:wght@400;500;700&display=swap" rel="stylesheet">
<style>
  :root {
    --stage: #e9e8e6;
    --card: #f7f7f6;
    --edge: #3f8a2e;
    --green: #3f8a2e;
    --brown: #9a6a1c;
    --ink: #2b2b2b;
    --rule: #555555;
  }
  * { box-sizing: border-box; margin: 0; padding: 0; }
  html, body { width: 1200px; height: 779px; overflow: hidden; }
  body {
    background: var(--stage);
    font-family: "Roboto", Arial, sans-serif;
    color: var(--ink);
    position: relative;
  }
  .card {
    position: absolute;
    background: var(--card);
    border-radius: 22px;
    border-bottom: 4px solid var(--edge);
    box-shadow: 0 6px 18px rgba(0,0,0,0.12);
  }

  /* Front */
  .card-front {
    left: 70px; top: 200px;
    width: 580px; height: 340px;
    display: flex; flex-direction: column; align-items: center; justify-content: center;
  }
  .brand {
    display: flex; align-items: center; gap: 14px;
    margin-bottom: 58px;
  }
  .brand-dot {
    width: 34px; height: 34px; border-radius: 50%;
    background: var(--green);
    flex: none;
  }
  .brand-name {
    font-weight: 500; font-size: 24px; color: var(--green);
    line-height: 1.15;
  }
  .front-web {
    font-size: 15px; letter-spacing: 4px; color: var(--ink);
  }

  /* Back */
  .card-back {
    left: 780px; top: 100px;
    width: 340px; height: 580px;
    display: flex; flex-direction: column; align-items: center;
    padding-top: 56px;
  }
  .back-brand {
    display: flex; flex-direction: column; align-items: center; gap: 12px;
    margin-bottom: 34px;
  }
  .back-brand .brand-dot { width: 64px; height: 64px; }
  .back-brand .brand-name { font-size: 20px; text-align: center; }
  .person-name {
    font-weight: 700; font-size: 25px; color: var(--green);
  }
  .person-role {
    font-size: 16px; color: var(--brown); margin-top: 4px;
  }
  .icon-row {
    display: flex; align-items: center; gap: 6px;
    margin-top: 22px;
  }
  .icon-row .dash { width: 12px; height: 1.5px; background: var(--rule); }
  .icon {
    width: 24px; height: 24px; border-radius: 50%;
    background: var(--green);
    display: flex; align-items: center; justify-content: center;
  }
  .contact-list {
    list-style: none; text-align: center; margin-top: 14px;
    font-size: 17px; line-height: 1.3;
  }
  .divider {
    width: 60px; height: 2px; background: var(--rule);
    margin: 30px 0 26px;
  }
  .address {
    font-style: normal; text-align: center;
    font-size: 19px; line-height: 1.3;
  }
</style>
</head>
<body>

<section class="card card-front" aria-label="Card front">
  <div class="brand">
    <span class="brand-dot" aria-hidden="true"></span>
    <span class="brand-name">Lone Maple Creek<br>Veterinary Hospital</span>
  </div>
  <p class="front-web">www.lmcr.net</p>
</section>

<section class="card card-back" aria-label="Card back">
  <div class="back-brand">
    <span class="brand-dot" aria-hidden="true"></span>
    <span class="brand-name">Lone Maple Creek</span>
  </div>

  <h1 class="person-name">Daniel Harper</h1>
  <p class="person-role">President</p>

  <div class="icon-row" aria-hidden="true">
    <span class="dash"></span>
    <span class="icon">
      <svg width="13" height="13" viewBox="0 0 24 24"><path fill="#fff" d="M6.6 10.8a15.1 15.1 0 0 0 6.6 6.6l2.2-2.2a1 1 0 0 1 1-.25 11.4 11.4 0 0 0 3.6.57 1 1 0 0 1 1 1V20a1 1 0 0 1-1 1A17 17 0 0 1 3 4a1 1 0 0 1 1-1h3.5a1 1 0 0 1 1 1c0 1.25.2 2.45.57 3.57a1 1 0 0 1-.25 1z"/></svg>
    </span>
    <span class="icon">
      <svg width="13" height="13" viewBox="0 0 24 24"><rect x="3" y="6" width="18" height="12" rx="1.5" fill="#fff"/><path d="M3.5 6.5l8.5 6.5 8.5-6.5" fill="none" stroke="#3f8a2e" stroke-width="1.8"/></svg>
    </span>
    <span class="icon">
      <svg width="13" height="13" viewBox="0 0 24 24" fill="none" stroke="#fff" stroke-width="2"><circle cx="12" cy="12" r="9"/><path d="M3 12h18M12 3c3 3 3 15 0 18M12 3c-3 3-3 15 0 18"/></svg>
    </span>
    <span class="dash"></span>
  </div>

  <ul class="contact-list">
    <li>(555) 204-7718</li>
    <li>info@lmcr.net</li>
    <li>www.lmcr.net</li>
  </ul>

  <div class="divider"></div>

  <address class="address">4820 Birchwood Lane,<br>Maple Falls, TX 75010</address>
</section>

</body>
</html>
```